Business Card Design Project

This is a new division in our company. "Kestrel Wellsite & Safety" This is a Oilfield Safety company. I have included our new logo. I also have given our other business card. We love double sided with lots of color. We like to stand out. Please DO NOT duplicate our other card and bring your design into it. See all attached files.
Reason: forgot to change this when I posted it.
Here is the correct information card.
www.kestrelwellsitesafety.example
Dwayne@kestrelwellsitesafety.example
Reason: revision for a few.
Reason: was traveling and need to review designs.
Target Market(s)
Oil and Gas industry. Masculine look.
Industry/Entity Type
Business
Look and feel

```html
<!DOCTYPE html>
<html lang="en">
<head>
<meta charset="utf-8">
<title>Kestrel Wellsite &amp; Safety — Business Card</title>
<link href="https://fonts.googleapis.com/css2?family=Arvo&family=Open+Sans&display=swap" rel="stylesheet">
<style>
  :root {
    --backdrop: #504f4f;
    --paper: #fbfbfb;
    --red: #ec2027;
    --orange-dark: #f26b35;
    --orange-light: #f9ad3c;
    --green-dark: #1f6a3a;
    --green: #3cb54a;
    --teal: #13b5ad;
    --ink: #161616;
    --white: #ffffff;
  }
  * { margin: 0; padding: 0; box-sizing: border-box; }
  html, body { width: 1200px; height: 1000px; overflow: hidden; }
  body { background: var(--backdrop); position: relative; font-family: "Arvo", serif; }

  .card {
    position: absolute;
    left: 310px;
    width: 596px;
    height: 324px;
    background: var(--paper);
    overflow: hidden;
  }
  .card--front { top: 136px; }
  .card--back { top: 526px; }

  .card__wave { position: absolute; inset: 0; width: 596px; height: 324px; }

  .address {
    position: absolute; left: 131px; top: 21px;
    font-size: 14px; color: var(--green-dark);
  }
  .brand {
    position: absolute; left: 44px; top: 60px;
    display: flex; align-items: center; gap: 12px;
  }
  .brand__mark { width: 18px; height: 18px; background: var(--red); flex: none; }
  .brand__name {
    font-size: 27px; line-height: 32px; color: var(--teal); font-weight: 400;
  }
  .emblem {
    position: absolute; left: 432px; top: 18px;
    width: 86px; height: 146px;
    border-radius: 6px;
    background: linear-gradient(180deg, var(--orange-light), var(--orange-dark));
    opacity: 0.85;
  }

  .contact { position: absolute; left: 27px; top: 153px; font-size: 17px; line-height: 23.5px; }
  .contact__name { color: var(--ink); font-size: 18px; }
  .contact__office { color: var(--orange-light); }
  .contact__fax { color: var(--orange-dark); }
  .contact__cell { color: var(--green); }
  .contact__email { color: var(--teal); }

  .hotline {
    position: absolute; right: 24px; bottom: 7px;
    font-family: "Open Sans", sans-serif; font-size: 20px; color: var(--white);
  }

  .website {
    position: absolute; left: 70px; top: 114px;
    font-family: "Open Sans", sans-serif; font-size: 30px; color: var(--ink);
    white-space: nowrap;
  }
  .website__accent { color: var(--teal); }
</style>
</head>
<body>

<section class="card card--front" aria-label="Business card front">
  <svg class="card__wave" viewBox="0 0 596 324" aria-hidden="true">
    <path d="M0,288 C90,312 300,310 440,268 C520,244 572,190 596,132 L596,324 L0,324 Z" fill="var(--orange-light)"/>
    <path d="M0,288 C90,312 300,310 445,274 C525,252 575,200 596,148 L596,324 L0,324 Z" fill="var(--orange-dark)"/>
    <path d="M0,288 C90,312 300,310 450,280 C530,262 578,212 596,162 L596,324 L0,324 Z" fill="var(--red)"/>
  </svg>

  <p class="address">4820 County Road 12, Alvin, TX 77511</p>

  <div class="brand">
    <span class="brand__mark"></span>
    <span class="brand__name">Kestrel Wellsite<br>&amp; Safety</span>
  </div>

  <div class="emblem" role="img" aria-label="Company emblem illustration"></div>

  <div class="contact">
    <p class="contact__name">Dwayne Harlow</p>
    <p class="contact__office">Office: 555-014-2210</p>
    <p class="contact__fax">Fax: 1-800-555-0147</p>
    <p class="contact__cell">Cell: 555-019-3386</p>
    <p class="contact__email">Email: Dwayne@kestrelwellsitesafety.example</p>
  </div>

  <p class="hotline">Call: 1-800-555-0199</p>
</section>

<section class="card card--back" aria-label="Business card back">
  <svg class="card__wave" viewBox="0 0 596 324" aria-hidden="true">
    <path d="M0,134 C40,220 210,292 440,306 C520,311 582,302 596,286 L596,324 L0,324 Z" fill="var(--orange-light)"/>
    <path d="M0,150 C45,230 215,294 440,306 C520,311 582,302 596,286 L596,324 L0,324 Z" fill="var(--orange-dark)"/>
    <path d="M0,164 C50,240 220,297 440,306 C520,311 582,302 596,286 L596,324 L0,324 Z" fill="var(--red)"/>
  </svg>

  <p class="website"><span class="website__accent">www.</span>kestrelwellsitesafety<span class="website__accent">.example</span></p>
</section>

</body>
</html>
```